Buchverlag sucht Cover-Design
Zielgruppe
Wir sind ein Buchverlag, der über Bravolo publizieren.
Unsere Zielgruppe sind: alle Selbstständigen, Unternehmern, Intrapreneuren, genauso wie Coaches, Experten, Start-ups und Entrepreneure.
Auch an diejenigen, die dieses Vorhaben angehen möchten.
Aufgabenstellung
Das Cover soll Nischen entsprechend sein. (Business Findung und Gestaltung)
Andersartig, auffallend, jedoch seriös sein.
Genaue Vorstellung:
Ein im freien Naturlandschaft fliegender Adler, der seine Beute fest im Blick hat und zielgenau seine Beute
zugreifen kann!
Den Schriftzug auffällig gestalten
Titel:
HOHE WARTE - Echter Reichtum gehört jedem von Anfang an
Untertitel:
Die klare Haltung der Vorreiter mit praktischem Wegweiser für Klarheit & Zufriedenheit bei privaten und beruflichen Weichenstellungen
Autor:
Velina Korbach
Logo des Verlags im Anhang
Name des Verlags:
Mond Quelle Verlag

```html
<!DOCTYPE html>
<html lang="de">
<head>
<meta charset="utf-8">
<title>Hohe Warte – Velina Korbach</title>
<link rel="stylesheet" href="https://fonts.googleapis.com/css2?family=Open+Sans:wght@400;600;700&family=Playfair+Display:wght@500&display=swap">
<style>
  :root {
    --sky: #9db1b4;
    --sky-light: #b9c6c6;
    --cloud: #cfd1cf;
    --cloud-deep: #b7bbb9;
    --rock: #7d7369;
    --rock-dark: #5e564f;
    --text: #ffffff;
    --ring: #8a8d8c;
    --ring-fill: #c9cbca;
  }
  html, body {
    margin: 0;
    padding: 0;
    overflow: hidden;
    background: #ffffff;
  }
  .cover {
    position: relative;
    width: 852px;
    height: 1200px;
    overflow: hidden;
    font-family: "Open Sans", Arial, sans-serif;
    color: var(--text);
  }
  .cover-photo {
    position: absolute;
    inset: 0;
    background:
      radial-gradient(ellipse 170px 330px at 90px 360px, rgba(94,86,79,0.85), rgba(125,115,105,0.4) 60%, transparent 100%),
      radial-gradient(ellipse 190px 380px at 760px 400px, rgba(94,86,79,0.85), rgba(125,115,105,0.4) 60%, transparent 100%),
      radial-gradient(ellipse 120px 200px at 300px 400px, rgba(125,115,105,0.55), transparent 100%),
      radial-gradient(ellipse 500px 260px at 420px 820px, rgba(215,217,215,0.9), transparent 100%),
      linear-gradient(180deg, var(--sky) 0%, var(--sky-light) 30%, var(--cloud-deep) 55%, var(--cloud) 75%, #c4c7c6 100%);
  }
  .author {
    position: absolute;
    left: 40px;
    top: 80px;
    margin: 0;
    font-size: 31px;
    font-weight: 600;
    letter-spacing: 0.2px;
  }
  .title {
    position: absolute;
    left: 0;
    right: 0;
    top: 110px;
    margin: 0;
    font-family: "Playfair Display", Georgia, serif;
    font-weight: 500;
    font-size: 218px;
    line-height: 212px;
    text-align: center;
    letter-spacing: -4px;
  }
  .title span { display: block; }
  .subtitle {
    position: absolute;
    left: 40px;
    right: 20px;
    top: 562px;
    margin: 0;
    font-size: 29px;
    font-weight: 400;
    letter-spacing: -0.3px;
  }
  .tagline {
    position: absolute;
    left: 40px;
    right: 30px;
    top: 650px;
    margin: 0;
    font-size: 18.5px;
    font-weight: 600;
    line-height: 28px;
  }
  .badge {
    position: absolute;
    left: 453px;
    top: 854px;
    width: 102px;
    height: 102px;
  }
  .publisher {
    position: absolute;
    left: 0;
    right: 0;
    bottom: 26px;
    display: flex;
    justify-content: center;
    align-items: center;
    gap: 12px;
  }
  .publisher-dot {
    width: 22px;
    height: 22px;
    border-radius: 50%;
    background: var(--text);
  }
  .publisher-name {
    font-size: 40px;
    font-weight: 700;
    letter-spacing: 0.5px;
  }
</style>
</head>
<body>
  <main class="cover">
    <div class="cover-photo" role="img" aria-label="Foto: schroffe Felsgipfel über einem Wolkenmeer, ein Adler gleitet links unten durch den Himmel"></div>

    <p class="author">Velina Korbach</p>

    <h1 class="title"><span>HOHE</span><span>WARTE</span></h1>

    <p class="subtitle">Echter Reichtum gehört jedem von Anfang an</p>

    <p class="tagline">Die klare Haltung der Vorreiter mit praktischem Wegweiser für Klarheit &amp; Zufriedenheit bei privaten und beruflichen Weichenstellungen</p>

    <svg class="badge" viewBox="0 0 102 102" aria-hidden="true">
      <circle cx="51" cy="51" r="49" fill="var(--ring-fill)" stroke="#555a59" stroke-width="2"/>
      <circle cx="51" cy="51" r="14" fill="var(--ring)" stroke="#4c504f" stroke-width="2"/>
    </svg>

    <div class="publisher">
      <span class="publisher-dot"></span>
      <span class="publisher-name">MQV</span>
    </div>
  </main>
</body>
</html>
```